Salmon Shop that sells both wholesale and retail salmon in a variety of ways.

"Harbour Fillet Co" is a business that is selling atlantic salmon in every way possible. We will be a salmon butcher to the public for retail purchase and we will also be out and about trying to sell our products to restaurants cafes and any other wholesale way. Our product is from Tasmania but we will be trading on the Sunshine Coast. The shop design has an urban, rustic feel and very much about the product. One of the owners has worked on salmon farms for 15 years and we want it to be very specialised and quality. I have nothing to offer you to help with this design....I would like both a salmon on the card, not sure if image or silohette is best and would like the other side to have a fillet with a tag of some sort. We are looking for a logo also. Use a photo of an Atlantic Salmon, Atlantic Salmon have two fins along the back.
Updates

Project Deadline Extended Reason: I am extending the deadline as I have still not got exactly what I want. All designers have added something great to what I am after and I just need someone to pull it all together. I have put in a new brief with a sketched image to help so we can get this perfect. Please read all the instructions. Thank you Added Monday, February 16, 2015

Target Market(s)

Restaurants, cafes

Industry/Entity Type

Retail

Contact Information for Business Card

Harbour Fillet Co (Not to have "Shop" at the end.Shop 12/130-164 Brisbane RdMooloolaba 4557

Colors
1c66ab

Requirements
Must have
• logo for harbour fillet Co with the S being salmon fillet of fresh salmon on white platemap of tasmaniasepia /black and white image of atlantic salmon
Nice to have
• fillet of salmonmap of tasmaniasalmon
Should not have
• Not Shop at the end.

```html
<!DOCTYPE html>
<html lang="en">
<head>
<meta charset="utf-8">
<title>Harbour Fillet Co – Business Card</title>
<link rel="stylesheet" href="https://fonts.googleapis.com/css2?family=Arimo:wght@400;700&display=swap">
<style>
  :root {
    --page: #ffffff;
    --wood-light: #d9a977;
    --wood-mid: #c38b59;
    --wood-dark: #a8703f;
    --salmon-light: #f2a27e;
    --salmon-dark: #8a4a3a;
    --fish-silver: #c9ccd0;
    --fish-dark: #5e6670;
    --accent-red: #d7262b;
    --ink: #1c1c1c;
    --ink-soft: #3a2d24;
    --card-edge: #d8d8d8;
  }
  * { margin: 0; padding: 0; box-sizing: border-box; }
  html, body {
    width: 1200px; height: 358px; overflow: hidden;
    background: var(--page);
    font-family: "Arimo", Arial, sans-serif;
  }
  .sheet { position: relative; width: 1200px; height: 358px; }

  .card {
    position: absolute; top: 11px; height: 338px;
    border: 1px solid var(--card-edge); overflow: hidden;
  }
  .card--front { left: 11px; width: 560px; }
  .card--back { left: 604px; width: 574px; background: var(--page); }

  .wood {
    position: absolute; inset: 0;
    background: linear-gradient(100deg, var(--wood-mid) 0%, var(--wood-light) 35%, var(--wood-mid) 60%, var(--wood-light) 80%, var(--wood-dark) 100%);
  }
  .front-art { position: absolute; inset: 0; }

  .brand-name {
    position: absolute; color: var(--ink);
    font-weight: 400; line-height: 1.05; letter-spacing: 0.5px;
    display: flex; align-items: center; gap: 14px;
  }
  .brand-name .mark {
    width: 18px; height: 18px; border-radius: 50%; background: var(--accent-red); flex: none;
  }
  .card--front .brand-name { left: 262px; top: 108px; font-size: 36px; }

  .address {
    position: absolute; left: 312px; top: 252px;
    font-size: 24px; line-height: 29px; color: var(--ink-soft);
  }

  .back-band { position: absolute; left: 0; top: 0; width: 100%; height: 150px; }
  .back-band .wood { bottom: 0; }
  .stripe { position: absolute; left: 0; width: 100%; background: var(--accent-red); }
  .stripe--thick { top: 102px; height: 9px; }
  .stripe--thin { top: 138px; height: 4px; }
  .card--back .brand-name { left: 130px; top: 36px; font-size: 40px; }

  .fish-photo { position: absolute; left: 125px; top: 168px; }
  .web {
    position: absolute; left: 0; width: 100%; top: 300px;
    text-align: center; font-size: 20px; color: var(--accent-red); letter-spacing: 0.3px;
  }
</style>
</head>
<body>
<main class="sheet">
  <section class="card card--front">
    <div class="wood" role="img" aria-label="Rustic timber board background"></div>
    <svg class="front-art" width="560" height="338" viewBox="0 0 560 338">
      <defs>
        <linearGradient id="steakTone" x1="0" y1="0" x2="1" y2="1">
          <stop offset="0" stop-color="var(--salmon-light)"/>
          <stop offset="0.55" stop-color="#e07f5e"/>
          <stop offset="1" stop-color="var(--salmon-dark)"/>
        </linearGradient>
      </defs>
      <path d="M0 0 H200 Q262 169 210 338 H0 Z" fill="url(#steakTone)" role="img" aria-label="Photo of fresh salmon steaks"/>
      <path d="M200 0 Q262 169 210 338" fill="none" stroke="var(--accent-red)" stroke-width="7"/>
    </svg>
    <h1 class="brand-name"><span class="mark"></span>harbour fillet Co</h1>
    <p class="address">Shop 7/210-236<br>Wattlebay Rd<br>Kirrawee 4812</p>
  </section>

  <section class="card card--back">
    <div class="back-band">
      <div class="wood" role="img" aria-label="Rustic timber board background"></div>
      <div class="stripe stripe--thick"></div>
      <div class="stripe stripe--thin"></div>
    </div>
    <h2 class="brand-name"><span class="mark"></span>harbour fillet Co</h2>
    <svg class="fish-photo" width="330" height="110" viewBox="0 0 330 110" role="img" aria-label="Photo of a whole Atlantic salmon">
      <defs>
        <linearGradient id="fishTone" x1="0" y1="0" x2="0" y2="1">
          <stop offset="0" stop-color="var(--fish-dark)"/>
          <stop offset="0.5" stop-color="var(--fish-silver)"/>
          <stop offset="1" stop-color="#eef0f2"/>
        </linearGradient>
      </defs>
      <rect x="0" y="0" width="330" height="110" rx="50" fill="url(#fishTone)"/>
    </svg>
    <p class="web">www.harbourfilletco.com.au</p>
  </section>
</main>
</body>
</html>
```